bright meadowline requires some business cards

I need some business cards created that feature the company's newly designed logo. The business cards need to be be double sided and be a standard Australian size of 90mm x 55mm

Target Market(s)

business professionals, company executives, local goverment

Industry/Entity Type

Business

Requirements
Must have
• Company's logo
• The information section must include
• Individual name:
• Position:
• Phone:
• Address:
• Email:
• Website: www.brightmeadowline.example
• The cards need to be easily formatted so I can enter staff members details positions etc...
• I plan to get these printed at deskhaven so can you please ensure that all designs meet their printing requirements http://www.deskhaven.example/retail/b2c/opsProductCreate.do?qty=1&cardQty=1000&sided=double&productname=colourbusinesscards&category=businesscards
Nice to have
• I might like to see some of the services we offer printed on one of the faces:
• Lighting Design (architectural, commercial, residential, theatrical ,exterior, interior) Lighting Consultancy, Theatrical Consultancy

```html
<!DOCTYPE html>
<html lang="en">
<head>
<meta charset="utf-8">
<title>bright meadowline – business cards</title>
<link rel="stylesheet" href="https://fonts.googleapis.com/css2?family=Questrial&family=Arimo:wght@400;700&display=swap">
<style>
  :root {
    --page-bg: #ffffff;
    --card-front-bg: #ffffff;
    --card-edge: #d6d6d6;
    --band-dark: #333333;
    --brand-blue: #3891d0;
    --wordmark-ink: #3a3a3a;
    --text-light: #ffffff;
  }
  * { margin: 0; padding: 0; box-sizing: border-box; }
  html, body {
    width: 1200px; height: 1000px; overflow: hidden;
    background: var(--page-bg);
  }
  .canvas { position: relative; width: 1200px; height: 1000px; }

  .card {
    position: absolute; top: 357px;
    width: 466px; height: 286px;
    overflow: hidden;
  }
  .card--front {
    left: 101px;
    background: var(--card-front-bg);
    border: 1px solid var(--card-edge);
  }
  .card--back {
    left: 633px;
    background: var(--brand-blue);
  }

  .brand {
    position: absolute; left: 60px; top: 118px;
    display: flex; align-items: center; gap: 14px;
  }
  .brand__dot {
    width: 22px; height: 22px; border-radius: 50%;
    background: var(--brand-blue);
  }
  .brand__name {
    font-family: "Questrial", sans-serif;
    font-size: 44px; line-height: 1;
    color: var(--wordmark-ink);
    letter-spacing: -0.5px;
  }

  .services-band {
    position: absolute; left: 0; right: 0; bottom: 0;
    height: 49px;
    background: var(--band-dark);
    color: var(--text-light);
    font-family: "Arimo", sans-serif;
    font-size: 11px; line-height: 13px;
    text-align: center;
    padding: 8px 24px 0;
  }

  .contact {
    position: absolute; left: 33px; top: 130px;
    color: var(--text-light);
    font-family: "Arimo", sans-serif;
  }
  .contact__name {
    font-weight: 700; font-size: 18px; line-height: 22px;
    margin-bottom: 9px;
  }
  .contact__line { font-size: 12px; line-height: 15px; }
  .contact__group { margin-bottom: 9px; }
</style>
</head>
<body>
<main class="canvas">
  <section class="card card--front" aria-label="Card front">
    <div class="brand">
      <span class="brand__dot" aria-hidden="true"></span>
      <span class="brand__name">bright meadowline</span>
    </div>
    <p class="services-band">Lighting Design (architectural, commercial, residential, theatrical ,exterior, interior) Lighting Consultancy, Theatrical Consultancy</p>
  </section>

  <section class="card card--back" aria-label="Card back">
    <div class="contact">
      <h1 class="contact__name">Daniel Harrowby</h1>
      <div class="contact__group">
        <p class="contact__line">+61 8 94418270</p>
      </div>
      <div class="contact__group">
        <p class="contact__line">daniel@brightmeadowline.example</p>
        <p class="contact__line">www.brightmeadowline.example</p>
      </div>
      <div class="contact__group">
        <p class="contact__line">PO Box 482, Perth</p>
        <p class="contact__line">WA 6000 Australia</p>
      </div>
    </div>
  </section>
</main>
</body>
</html>
```